Finance Product Agency Business Card Design

We're an agency that provides products (service contracts, gap insurance, tire and wheel, etc) and support to dealership finance departments. We specialize in training finance producers to maximize their potential and also keep them up to date on the ever changing compliance and legal landscape. I'll attach an image of our logo, excited to see what you all come up with. Would also be interested in discussing our new website design with the winner.

Target Market(s)

auto dealerships

Industry/Entity Type

Business

Contact Information for Business Card

Mark Dolvery
Phone 317.624.5583
Fax 855.472.3308
email Mark.Dolvery@brightlanecoverage.example

Requirements
Must have
• basic contact information
Nice to have
• looking for something professional but modern

```html
<!DOCTYPE html>
<html lang="en">
<head>
<meta charset="utf-8">
<title>Brightlane Coverage – Business Card</title>
<link href="https://fonts.googleapis.com/css2?family=Open+Sans:wght@400;600;700&display=swap" rel="stylesheet">
<style>
  :root {
    --stage: #2b2b2d;
    --teal: #3b5d6e;
    --teal-deep: #2c4857;
    --paper: #f7f7f7;
    --paper-shade: #e9e9e9;
    --ink: #444a4e;
    --faint: #d9dcde;
    --white: #ffffff;
  }
  * { box-sizing: border-box; margin: 0; padding: 0; }
  html, body {
    width: 1200px; height: 900px; overflow: hidden;
    background: var(--stage);
    font-family: "Open Sans", Arial, sans-serif;
  }
  .stage {
    position: relative; width: 1200px; height: 900px;
    display: flex; flex-direction: column; align-items: center; justify-content: center; gap: 40px;
  }
  .card {
    position: relative; width: 700px; height: 400px; overflow: hidden;
    box-shadow: 0 12px 30px rgba(0,0,0,.45);
  }
  /* back side */
  .card-back {
    background: linear-gradient(160deg, var(--teal) 0%, var(--teal-deep) 100%);
    display: flex; align-items: center; justify-content: center; gap: 22px;
  }
  .brand-dot {
    width: 64px; height: 64px; border-radius: 50%;
    background: var(--white);
  }
  .brand-name {
    font-weight: 700; font-size: 44px; letter-spacing: 1px;
    text-transform: uppercase; color: var(--white); line-height: 1;
  }
  /* front side */
  .card-front {
    background: linear-gradient(180deg, var(--white) 0%, var(--paper) 45%, var(--paper-shade) 62%);
  }
  .front-brand {
    position: absolute; top: 64px; right: 44px;
    display: flex; align-items: center; gap: 14px;
  }
  .front-brand .brand-dot { width: 40px; height: 40px; background: var(--teal); }
  .front-brand .brand-name { font-size: 28px; color: var(--teal-deep); }
  .faint-mark {
    position: absolute; top: 50px; left: 80px;
    width: 130px; height: 130px; border-radius: 50%;
    background: var(--faint);
  }
  .holder-name {
    position: absolute; left: 40px; top: 196px;
    font-size: 27px; font-weight: 600; color: var(--ink);
  }
  .rule {
    position: absolute; left: 0; right: 0; top: 246px; height: 5px;
    background: var(--teal);
  }
  .contact-band {
    position: absolute; left: 0; right: 0; top: 257px; bottom: 0;
    background: linear-gradient(180deg, var(--teal) 0%, var(--teal-deep) 100%);
    padding: 22px 40px 0;
    list-style: none;
  }
  .contact-row {
    display: flex; align-items: center; gap: 22px;
    height: 36px; color: var(--white); font-size: 19px;
  }
  .contact-row svg { width: 20px; height: 20px; fill: var(--white); flex: none; }
</style>
</head>
<body>
<main class="stage">
  <section class="card card-back" aria-label="Card back">
    <span class="brand-dot"></span>
    <span class="brand-name">Brightlane Coverage</span>
  </section>

  <section class="card card-front" aria-label="Card front">
    <div class="faint-mark"></div>
    <div class="front-brand">
      <span class="brand-dot"></span>
      <span class="brand-name">Brightlane Coverage</span>
    </div>
    <h1 class="holder-name">Mark Dolvery</h1>
    <div class="rule"></div>
    <ul class="contact-band">
      <li class="contact-row">
        <svg viewBox="0 0 24 24" aria-hidden="true"><path d="M6.6 10.8a15.1 15.1 0 0 0 6.6 6.6l2.2-2.2a1 1 0 0 1 1-.25 11.4 11.4 0 0 0 3.6.57 1 1 0 0 1 1 1V20a1 1 0 0 1-1 1A17 17 0 0 1 3 4a1 1 0 0 1 1-1h3.5a1 1 0 0 1 1 1c0 1.25.2 2.45.57 3.57a1 1 0 0 1-.25 1z"/></svg>
        <span>317.624.5583</span>
      </li>
      <li class="contact-row">
        <svg viewBox="0 0 24 24" aria-hidden="true"><path d="M7 3h10v5H7zM4 9h16a2 2 0 0 1 2 2v6h-4v4H6v-4H2v-6a2 2 0 0 1 2-2zm4 7v3h8v-3z"/></svg>
        <span>855.472.3308</span>
      </li>
      <li class="contact-row">
        <svg viewBox="0 0 24 24" aria-hidden="true"><path d="M3 6h18v12H3zm2 2v.4l7 4.6 7-4.6V8l-7 4.5z"/></svg>
        <span>Mark.Dolvery@brightlanecoverage.example</span>
      </li>
    </ul>
  </section>
</main>
</body>
</html>
```